Creative, Fun, Eye catching Signage project showcasing our fabulous services

Please take into consideration the garage door is in small squares and submit your design showing this .Check out the image that shows the front of the office with the current sign that is over the front door as well as the glass roller door where we would like the new sign. I would like to see the words for each service in a separate square with a black background where the writing stands out. I would like to see the clouds incorporated into the design so it works with the sign above the door. The goal of this project is to create clear, engaging, and informative signage that showcases our company's services. The signage should be designed to be easily read and understood by a diverse audience, ensuring everyone can access information about the available services. We would like it to have a simple yet strong visual appeal and incorporate visual elements that enhance the attractiveness of the signage and capture attention. The sign will go on the garage door (the image has been attached ). The door is made up of 16 glass squares.
The services we would like advertised is
Support Workers
Social Groups
Living Skills Programs
Supported Holidays
Respite
Occupational Therapy
Exercise Physiology
Positive Behavioural Support

I think we would prefer the words to stand out not images, where the titles are the most obvious thing people see with black backgrounds and pops of our colours.

I have attached some of our flyers to give you an idea of the design we love. We love black backgrounds, a font that is easy to read and jumps out. We don't want to design to be too busy. We would like to to be fun!
The current drop off zone sign stays so we would like something that works in and compliments that

We love our clients with disabilities, they are very special to us, we would like them to be able to see all of the different things we can help them out with.
Updates

Sick

Target Market(s)

Our target market is parents, carers and professionals who assist people with disabilities to find support

Industry/Entity Type

Community Services/Disability Supports

Colors
0054AA
0677BA
7BADD7
CADEEF
E8F1F8
FFF300
FFF600
FEFA6F
FFFEC7
FFFEE8
E54698
E96AAD
F1A4CE
F9D9EA
FCEFF6

Requirements
Must have
• Clear writing and not busy design that is easy to read when driving past
Should not have
• Colours that are not our branding colours

```html
<!DOCTYPE html>
<html lang="en">
<head>
<meta charset="utf-8">
<title>Services Door Signage</title>
<link rel="stylesheet" href="https://fonts.googleapis.com/css2?family=Mouse+Memoirs&display=swap">
<style>
  :root {
    --page: #efeae0;
    --frame: #d6cdb4;
    --panel: #1c1c1c;
    --glass-top: #4f5866;
    --glass-bottom: #2f353e;
    --ring-red: #e8485f;
    --ring-blue: #3b9be2;
    --ring-yellow: #f6dc33;
    --text: #ffffff;
    --drop-yellow: #fff300;
    --drop-blue: #1fa0f0;
    --drop-bg-top: #05070d;
    --drop-bg-bottom: #0a1430;
    --cloud: #ffffff;
    --cloud-shade: #e8f1f8;
  }
  * { box-sizing: border-box; margin: 0; padding: 0; }
  html, body { width: 1200px; height: 1200px; overflow: hidden; background: var(--page); }
  .door {
    position: absolute; left: 26px; top: 26px;
    width: 1148px; height: 1148px;
    background: var(--frame);
    border: 14px solid var(--frame);
    display: grid;
    grid-template-columns: repeat(4, 268px);
    grid-template-rows: repeat(4, 268px);
    gap: 16px;
  }
  .tile { position: relative; width: 268px; height: 268px; overflow: hidden; }
  .glass { background: linear-gradient(160deg, var(--glass-top), var(--glass-bottom)); }
  .service { background: var(--panel); }
  .service .ring { position: absolute; inset: 0; width: 100%; height: 100%; }
  .service .ring circle { fill: none; stroke-width: 9; stroke-linecap: round; }
  .ring-red circle { stroke: var(--ring-red); }
  .ring-blue circle { stroke: var(--ring-blue); }
  .ring-yellow circle { stroke: var(--ring-yellow); }
  .label {
    position: absolute; inset: 0;
    display: flex; flex-direction: column; align-items: center; justify-content: center;
    font-family: "Mouse Memoirs", sans-serif; color: var(--text);
    text-transform: uppercase; text-align: center; line-height: 0.92;
  }
  .label span { display: block; }
  .size-xs { font-size: 44px; }
  .size-s { font-size: 50px; }
  .size-m { font-size: 64px; }
  .size-l { font-size: 78px; }

  .drop-off {
    background: linear-gradient(180deg, var(--drop-bg-top), var(--drop-bg-bottom));
    border-top: 14px solid var(--drop-yellow);
  }
  .drop-off .sun-art {
    position: absolute; left: 50%; top: 22px; width: 44px; height: 44px;
    margin-left: 0;
    background: radial-gradient(closest-side, var(--drop-yellow), rgba(255,243,0,0.6) 55%, rgba(255,243,0,0) 100%);
  }
  .drop-off .wording {
    position: absolute; left: 0; right: 0; top: 70px;
    text-align: center; font-family: "Mouse Memoirs", sans-serif; line-height: 1;
  }
  .drop-off .brand { color: var(--text); font-size: 42px; text-transform: uppercase; }
  .drop-off .drop { color: var(--drop-yellow); font-size: 48px; }
  .drop-off .zone { color: var(--drop-blue); font-size: 48px; }
  .drop-off .cloud-art {
    position: absolute; left: 0; right: 0; bottom: 0; height: 56px;
    background: linear-gradient(180deg, rgba(232,241,248,0) 0%, var(--cloud-shade) 45%, var(--cloud) 100%);
  }
</style>
</head>
<body>
<div class="door">
  <div class="tile service">
    <svg class="ring ring-blue" viewBox="0 0 268 268"><circle cx="134" cy="134" r="114"/></svg>
    <div class="label size-xs"><span>Positive</span><span>Behavioural</span><span>Support</span></div>
  </div>
  <div class="tile glass"></div>
  <div class="tile service">
    <svg class="ring ring-red" viewBox="0 0 268 268"><circle cx="134" cy="134" r="114"/></svg>
    <div class="label size-m"><span>Support</span><span>Workers</span></div>
  </div>
  <div class="tile glass"></div>

  <div class="tile glass"></div>
  <div class="tile service">
    <svg class="ring ring-yellow" viewBox="0 0 268 268"><circle cx="134" cy="134" r="114"/></svg>
    <div class="label"><span class="size-m">Exercise</span><span class="size-s">Physiology</span></div>
  </div>
  <div class="tile glass"></div>
  <div class="tile service">
    <svg class="ring ring-blue" viewBox="0 0 268 268"><circle cx="134" cy="134" r="114"/></svg>
    <div class="label size-s"><span>Living</span><span>Skills</span><span>Programs</span></div>
  </div>

  <div class="tile service">
    <svg class="ring ring-red" viewBox="0 0 268 268"><circle cx="134" cy="134" r="114"/></svg>
    <div class="label size-l"><span>Respite</span></div>
  </div>
  <div class="tile drop-off">
    <div class="sun-art" role="img" aria-label="Small yellow sun illustration"></div>
    <div class="wording">
      <div class="brand">Brightwell</div>
      <div class="drop">Drop-Off</div>
      <div class="zone">Zone</div>
    </div>
    <div class="cloud-art" role="img" aria-label="Illustration of white clouds along the bottom edge"></div>
  </div>
  <div class="tile service">
    <svg class="ring ring-red" viewBox="0 0 268 268"><circle cx="134" cy="134" r="114"/></svg>
    <div class="label size-s"><span>Supported</span><span>Holidays</span></div>
  </div>
  <div class="tile glass"></div>

  <div class="tile glass"></div>
  <div class="tile service">
    <svg class="ring ring-blue" viewBox="0 0 268 268"><circle cx="134" cy="134" r="114"/></svg>
    <div class="label"><span class="size-xs">Occupational</span><span class="size-m">Therapy</span></div>
  </div>
  <div class="tile glass"></div>
  <div class="tile service">
    <svg class="ring ring-yellow" viewBox="0 0 268 268"><circle cx="134" cy="134" r="114"/></svg>
    <div class="label size-m"><span>Social</span><span>Groups</span></div>
  </div>
</div>
</body>
</html>
```